PIPE RELINING COMPANY NEEDS A NEW INFORMATIVE FLYER CREATED

We are a company that sells a service to residential homeowners (using a particular state of the art international product) and we need to refresh our A4 tri- fold flyer (z fold 6 pages). The layout needs to include pictures, heading and text boxes, but be simple and clean cut at the same time.

The front of the flyer must have the attached picture of the pipe under the house, logo and website.

This flyer is going to be given to clients and to leave with them when we quote for work.

Our colour scheme is black, white, red. A highlight colour if needed (in small amounts) could be 100% cyan and also a bright orange.

I have attached the copy of the text and this can be spread out throughout the brochure.

We are a professional and industry leading company so it needs to be professional, clean cut but with a modern edge.

Target Market(s)

HOMEOWNERS

Industry/Entity Type

It Company

Font styles to use
Sans Serif

Colors
ec1f27
ffffff
000000
f37122

Requirements
Must have
• PROFESSINAL, MODERN
• USE OF BLACK, RED AND WHITE - REFER LOGO
Should not have
• BE CLUTTERED

```html
<!DOCTYPE html>
<html lang="en">
<head>
<meta charset="utf-8">
<title>Clearline Relining – Pipe Relining Flyer</title>
<link href="https://fonts.googleapis.com/css2?family=Alegreya+Sans+SC:wght@700;800&family=Lato:wght@400;700;900&display=swap" rel="stylesheet">
<style>
:root{
  --red:#d8232a;
  --red-deep:#c41a20;
  --ink:#3a3a3a;
  --dark:#222;
  --grey:#f1f1f1;
  --white:#fff;
  --scene-a:#8fae7a;
  --scene-b:#8a6a4c;
  --dig-a:#d6c7ad;
  --dig-b:#b99268;
}
*{margin:0;padding:0;box-sizing:border-box}
html,body{width:848px;height:1200px;overflow:hidden;background:var(--white)}
body{font-family:"Lato",sans-serif;color:var(--ink);font-size:8.6px;line-height:1.27}
.flyer{position:relative;width:848px;height:1200px;overflow:hidden}
.panel{position:absolute;width:283px;height:598px;overflow:hidden;background:var(--white)}
.panel.grey{background:linear-gradient(180deg,#e9e9e9,#f6f6f6 60%,#efefef)}
.p-tl{left:0;top:0}.p-tm{left:283px;top:0}.p-tr{left:566px;top:0}
.p-bl{left:0;top:602px}.p-bm{left:283px;top:602px}.p-br{left:566px;top:602px}
.h{font-family:"Alegreya Sans SC",sans-serif;font-weight:800;color:var(--red);font-size:12.5px;letter-spacing:.2px;line-height:1.15;display:inline-block;padding-right:6px;border-bottom:1px solid var(--red);margin-bottom:4px;position:relative}
.h::after{content:"";position:absolute;right:-3px;bottom:-2.5px;width:4px;height:4px;border:1px solid var(--red);border-radius:50%;background:#fff}
.h.plain{font-family:"Lato",sans-serif;font-weight:700;font-size:13px;border:0}
.h.plain::after{display:none}
.block{position:absolute;left:22px;right:20px}
.block p{margin-bottom:3px}
.caps{text-transform:uppercase;font-size:8.2px}
.red{color:var(--red);font-weight:700}
.strong-note{font-weight:900;font-size:7px;text-transform:uppercase;letter-spacing:.4px;color:var(--dark);line-height:1.2}
.deco{position:absolute;border-radius:50%}
.ring{position:absolute;border-radius:50%;border:6px solid var(--red);overflow:hidden}
.fill{width:100%;height:100%}
.scene{background:radial-gradient(circle at 40% 30%,var(--scene-a),var(--scene-b))}
.arrows{list-style:none}
.arrows li{position:relative;padding-left:18px;margin-bottom:4px}
.arrows li::before{content:"→";position:absolute;left:0;top:-1px;color:var(--red);font-size:10px}
.arrows.grey li::before{color:#888}
.contact{position:absolute;left:0;right:0;text-align:center;font-size:9.4px;color:var(--ink)}
.contact .row{margin-bottom:14px}
.contact svg{display:block;margin:0 auto 5px}
.contact b{font-weight:700}
.title{position:absolute;left:22px;top:112px;font-family:"Alegreya Sans SC",sans-serif;font-weight:800;color:var(--red);font-size:50px;line-height:.9;letter-spacing:.5px}
.subtitle{position:absolute;left:23px;top:206px;font-size:10px;letter-spacing:8.2px;color:#333}
.brand{position:absolute;right:22px;top:40px;display:flex;align-items:center;gap:6px;font-family:"Lato",sans-serif;font-weight:900;font-size:20px;color:var(--dark);letter-spacing:-.3px}
.brand .dot{width:12px;height:12px;border-radius:50%;background:var(--red)}
.badge{position:absolute;left:177px;top:246px;width:70px;height:70px;border-radius:50%;background:#fff;border:4px solid #333;box-shadow:0 2px 5px rgba(0,0,0,.25);text-align:center;font-family:"Alegreya Sans SC",sans-serif;color:var(--red);line-height:1}
.badge b{display:block;font-size:21px;margin-top:13px}
.badge span{font-size:7px;font-weight:700}
.ba-label{position:absolute;font-weight:900;color:#fff;font-size:13px}
</style>
</head>
<body>
<div class="flyer">

  <section class="panel p-tl">
    <div class="deco" style="left:250px;top:142px;width:55px;height:55px;background:#f6dede"></div>
    <div class="block" style="top:20px">
      <h3 class="h">We have state of the art equipment</h3>
      <p>Our truck is custom designed and fully equipped with latest technology to carry out pipe relining.</p>
    </div>
    <div class="block" style="top:73px">
      <h3 class="h">We're Fully licensed &amp; Insured</h3>
      <p>All of our technicians are fully licensed and qualified to complete the job. Our company is fully insured and are happy to provide you with documentation.</p>
    </div>
    <div class="block" style="top:136px">
      <h3 class="h">We're Fully licensed &amp; Insured</h3>
      <p>All of our technicians are fully licensed and qualified to complete the job. Our company is fully insured and are happy to provide you with documentation.</p>
    </div>
    <div class="block" style="top:199px">
      <h3 class="h">After Sales Service</h3>
      <p>We don't forget about you after the job and as part of the warranty we carry out an annual camera inspection of the drainage.</p>
    </div>
    <div class="block" style="top:263px">
      <h3 class="h">Why It Works:</h3>
      <p class="caps">Clearline uses epoxy resin not polyester or silicate resins.</p>
      <p>Why? Because epoxy resin does not shrink. Polyester and silicate resins can shrink in the pipe allowing tree roots to return.</p>
      <p class="caps">Clearline inverts the liner instead of using a drag-in method.</p>
      <p>Why? Because this means that the resin has contact with the host pipe impregnating the cracks and joins the pipework. With the drag in method, the resin does not have contact with the host pipe and cannot impregnate the cracks and joins.</p>
      <p class="caps">Clearline uses a German system called Flexaliner.</p>
      <p>Why? Because it has been extensively tested in Europe and came out as the test winner in standard and extreme conditions based on all assessment criteria – effectiveness, density and load carrying capacity. Flexaliner has a proven track record and been used to reline hundreds of kms throughout Europe.</p>
      <p class="caps">Clearline provides a <span class="red">25 year</span> warranty</p>
      <p>Why? Because we understand the quality of the equipment and product and how we install it. We were one of the first to reline in NSW and are constantly carrying out research and development.</p>
    </div>
  </section>

  <section class="panel p-tm grey">
    <h2 style="position:absolute;left:0;right:0;top:64px;text-align:center;color:var(--red);font-weight:400;font-size:15px">Map</h2>
    <div class="deco" style="left:190px;top:72px;width:18px;height:18px;background:#ddd"></div>
    <div class="deco" style="left:195px;top:88px;width:30px;height:30px;background:#e2e2e2"></div>
    <div class="deco" style="left:224px;top:302px;width:20px;height:20px;background:#e0e0e0"></div>
    <div class="ring" style="left:25px;top:96px;width:232px;height:232px">
      <div class="fill" role="img" aria-label="Street map showing the office location" style="background:radial-gradient(circle at 45% 50%,#f4f4f4,#dcdcdc)"></div>
    </div>
    <div class="deco" style="left:22px;top:100px;width:28px;height:28px;background:#d9d9d9"></div>
    <div class="deco" style="left:46px;top:278px;width:42px;height:42px;background:radial-gradient(circle at 35% 35%,#f03a3f,var(--red-deep))"></div>
    <h2 style="position:absolute;left:0;right:0;top:368px;text-align:center;color:var(--red);font-weight:700;font-size:15px">CONTACT US</h2>
    <div class="contact" style="top:416px">
      <div class="row">
        <svg width="9" height="11" viewBox="0 0 9 11"><path d="M4.5 0C2 0 0 2 0 4.3 0 7.5 4.5 11 4.5 11S9 7.5 9 4.3C9 2 7 0 4.5 0z" fill="#d8232a"/><circle cx="4.5" cy="4.3" r="1.6" fill="#fff"/></svg>
        14 Harbour Lane, Eastwood NSW 2122
      </div>
      <div class="row">
        <svg width="10" height="10" viewBox="0 0 10 10"><path d="M2 0l2 2.4-1.2 1.3c.6 1.4 1.7 2.5 3.2 3.3L7.3 5.8 10 7.8 8.7 10C4 9.6.4 6 0 1.3z" fill="#d8232a"/></svg>
        02 9000 4417
      </div>
      <div class="row">
        <svg width="10" height="8" viewBox="0 0 10 8"><rect width="10" height="8" rx="1" fill="#d8232a"/><path d="M0 .6l5 3.6L10 .6" stroke="#fff" fill="none" stroke-width=".9"/></svg>
        <b>sam@clearlinerelining.com.au</b>
      </div>
      <div class="row">
        <svg width="11" height="11" viewBox="0 0 11 11" fill="none" stroke="#d8232a" stroke-width=".9"><circle cx="5.5" cy="5.5" r="5"/><ellipse cx="5.5" cy="5.5" rx="2.2" ry="5"/><path d="M.5 5.5h10M1.3 3h8.4M1.3 8h8.4"/></svg>
        www.clearlinerelining.com.au
      </div>
    </div>
  </section>

  <section class="panel p-tr" style="background:linear-gradient(180deg,#fff,#f3f3f3)">
    <div class="brand"><span class="dot"></span>Clearline Relining</div>
    <h1 class="title">Pipe<br>Relining</h1>
    <div class="subtitle">SYDNEY WIDE</div>
    <div class="deco" style="left:136px;top:256px;width:14px;height:14px;background:#e2e2e2"></div>
    <div class="deco" style="left:148px;top:250px;width:10px;height:10px;background:#ddd"></div>
    <div class="ring" style="left:21px;top:266px;width:256px;height:268px;border-width:8px">
      <div class="fill scene" role="img" aria-label="Cross-section of a house with tree roots growing around a relined drain pipe"></div>
    </div>
    <div class="badge"><b>24/7</b><span>Hours Service</span></div>
    <div class="deco" style="left:19px;top:478px;width:62px;height:62px;background:radial-gradient(circle at 35% 35%,#f03a3f,var(--red-deep))"></div>
  </section>

  <section class="panel p-bl">
    <div class="deco" style="left:-14px;top:-14px;width:36px;height:36px;background:#f6dede"></div>
    <div class="block" style="top:26px">
      <p>Sewers back up in properties due to ageing lines, misaligned joints, root infestation, calcification and ground movement, costing property owners thousands of dollars in damage to their homes and landscaping.</p>
      <p>Pipe relining eliminates the need for costly excavations to expose and replace this damaged pipework.</p>
      <p>Pipe Relining is the process of installing a new pipe within the old.</p>
      <p class="strong-note" style="margin-top:8px">Why replace all of your drainage pipes when you can permanently repair the broken sections without destroying your environment.</p>
    </div>
    <div class="block" style="top:163px">
      <h3 class="h">What Does Pipe Relining Mean?</h3>
      <p>Pipe relining is the method of repairing existing pipework from within the pipe itself. This is done by using the latest technology to insert a strong internal liner inside the existing pipe.</p>
      <p>During this process the resin impregnated side of the liner is pressed against the wall of the original host pipe at a specified pressure. This pressure ensure 100% resin contact and extrudes resin into all pipe joints, cracks and breaks ensuring no future tree root ingress or pipe movement is possible.</p>
      <p>Pipe relining can be undertaken in either short sectional repair, or long lengths utilising the inversion relining method.</p>
    </div>
    <div class="block" style="top:352px">
      <h3 class="h">Which Problems Can Pipe<br>Relining Repair?</h3>
      <p>Pipe relining can repair broken, cracked or root infested pipes, pipes with missing sections and pipes that continually block.</p>
      <p>No matter if the pipes are vertical, horizontal or concealed, they all can be repaired. Sections of broken pipes can be relined, without having to replace the entire pipeline.</p>
    </div>
    <div class="ring" style="left:-4px;top:488px;width:136px;height:136px;border-width:7px">
      <div class="fill" role="img" aria-label="Camera view inside a damaged pipe before relining" style="background:radial-gradient(circle at 50% 55%,#3a2418,#8a5a44)"></div>
    </div>
    <span class="ba-label" style="left:47px;top:500px">Before</span>
    <div class="deco" style="left:108px;top:488px;width:34px;height:34px;background:radial-gradient(circle at 35% 35%,#f03a3f,var(--red-deep))"></div>
    <div class="ring" style="left:140px;top:488px;width:136px;height:136px;border-width:7px">
      <div class="fill" role="img" aria-label="Camera view inside the same pipe after relining" style="background:radial-gradient(circle at 50% 55%,#1e3f1a,#4a8a3a)"></div>
    </div>
    <span class="ba-label" style="left:190px;top:500px">After</span>
    <div class="deco" style="left:240px;top:488px;width:34px;height:34px;background:#ececec"></div>
  </section>

  <section class="panel p-bm grey">
    <div class="deco" style="left:230px;top:-22px;width:52px;height:52px;background:#f4dcdc"></div>
    <div class="block" style="top:24px;left:22px">
      <h3 class="h plain" style="color:var(--red)">Patch Repair Process
        <svg width="38" height="20" viewBox="0 0 38 20" style="vertical-align:-5px;margin-left:8px"><rect x="1" y="8" width="36" height="8" fill="#bbb"/><rect x="13" y="6" width="12" height="12" fill="#888"/><path d="M19 0v4M13 2l2 3M25 2l-2 3" stroke="#d8232a" stroke-width="1.2"/></svg>
      </h3>
      <ul class="arrows grey" style="margin-top:4px">
        <li>Clean the line with a high pressure water jetter, and carry out a camera inspection to determine the exact location and cause of the problems.</li>
        <li>Prepare the liner. Cut the liner to the correct length, mix the appropriate amount of resin and impregnate the resin into the liner.</li>
        <li>Invert the liner into the pipe, inflate and then cure.</li>
        <li>A seamless, flexible liner is cut to length and filled with environmentally safe epoxy resin. The liner is then inverted into the existing, host pipe and inflated using compressed air. Once the liner is fully cured with hot water, it is ready for use.</li>
        <li>The result is a completely new pipe inside the old. This pipe within a pipe is 100% water tight, stronger than PVC pipe, and has an increased flow rate compared to most existing pipes. Relined pipes have a life expectancy of 50 years and our installation work has a 25 year guarantee.</li>
      </ul>
    </div>
    <div class="block" style="top:296px">
      <h3 class="h">Benefits of Pipe Relining</h3>
      <p>Quick Installation – Most relining jobs can be completed in the same day-without the mess and disruption of excavation.</p>
      <p>Long Life Product – Pipe Relining is a long term solution with a 50 year life expectancy.</p>
      <p>Minimal Disruption – save your landscapes, trees and driveways.</p>
      <p>Economical – Save on the cost, time and hassle of restoring your property and landscaping.</p>
      <p>Installation Guarantee – Clearline offer a</p>
      <p style="width:138px">25 year warranty, twice that of standard excavations. This also includes an annual warranty camera inspection.</p>
      <p class="strong-note" style="width:130px;margin-top:14px;letter-spacing:1px">Provides a solution to the whole problem, not just temporary relief from the symptoms.</p>
    </div>
    <div class="deco" style="left:236px;top:436px;width:42px;height:42px;background:#f7f7f7;box-shadow:0 0 0 1px #e6e6e6"></div>
    <div class="ring" style="left:150px;top:460px;width:138px;height:138px;border-width:6px">
      <div class="fill scene" role="img" aria-label="House cross-section with roots around the relined pipe"></div>
    </div>
    <div class="deco" style="left:152px;top:562px;width:34px;height:34px;background:radial-gradient(circle at 35% 35%,#f03a3f,var(--red-deep))"></div>
  </section>

  <section class="panel p-br" style="background:linear-gradient(180deg,#fff,#f2f2f2)">
    <div class="ring" style="left:18px;top:-72px;width:290px;height:262px;border-width:7px">
      <div class="fill" role="img" aria-label="Illustration of a relining system installed underground beside a house" style="background:radial-gradient(circle at 45% 35%,var(--dig-a),var(--dig-b))"></div>
    </div>
    <div class="deco" style="left:190px;top:174px;width:24px;height:24px;background:radial-gradient(circle at 35% 35%,#f03a3f,var(--red-deep))"></div>
    <div class="deco" style="left:38px;top:160px;width:18px;height:18px;background:#ddd"></div>
    <div class="deco" style="left:52px;top:152px;width:12px;height:12px;background:#e4e4e4"></div>
    <div class="deco" style="left:240px;top:184px;width:30px;height:30px;background:#ececec"></div>
    <div class="block" style="top:206px;left:22px">
      <h3 class="h">What Does Pipe Relining Mean?</h3>
      <ul class="arrows" style="margin-top:2px">
        <li>Permanent jointless liner</li>
        <li>50 years life expectancy</li>
        <li>Up front price</li>
        <li>Environmentally sound</li>
        <li>Eliminates structural disturbances</li>
        <li>Impervious to future root penetration</li>
        <li>Provides increased flow characteristics</li>
        <li>Suitable for industrial, residential and commercial applications</li>
      </ul>
      <p style="font-weight:700;font-size:10px;color:#333;margin-top:4px">Things You Should Know
        <svg width="38" height="26" viewBox="0 0 38 26" style="vertical-align:-8px;margin-left:14px"><circle cx="9" cy="14" r="4" fill="#d8232a"/><path d="M2 26c0-5 3-7 7-7s7 2 7 7z" fill="#d8232a"/><path d="M20 10c-2-5 4-8 8-6 3-3 9 0 7 4 2 3-2 6-5 4-3 2-8 1-9-1z" fill="none" stroke="#d8232a" stroke-width="1.2"/></svg>
      </p>
    </div>
    <div class="block" style="top:400px">
      <h3 class="h">Knowledge &amp; Experience</h3>
      <p>We train other plumbers and have been doing it for over 10 years.</p>
    </div>
    <div class="block" style="top:452px">
      <h3 class="h" style="padding-right:22px">We're An Owned &amp; Operated Business</h3>
      <p>We take great pride in our work. Our business is based on relationships not transactions.</p>
    </div>
    <div class="block" style="top:508px">
      <h3 class="h" style="padding-right:24px">We Use the best in class pipe relining<br>solution</h3>
      <p>We have sourced the best products and equipment from around the world and our Flexaliner product is from Germany.</p>
    </div>
  </section>

</div>
</body>
</html>
```